4 x Designs Required

Hi There,
I require 4 x different designs to be made for 4 new brands of mine however they can be quite interchangeable. HR Plinkr and Marketing Plinkr can be similar just with a difference in colour. The same goes for the Bulletin brands. This means there are ultimately two designs that need perfecting.

There must be a click here CTA on the banner somewhere. :-)

I require the banners in 728x90 format and 960x90 please.

Please use strap lines on the banners such as:
Essential Whitepapers for HR Professionals
Essential Whitepapers for Marketing Professionals
Your No.1 Whitepaper Resource

The brand names:
HR Plinkr
Marketing Plinkr
HR Dispatchly
Marketing Dispatchly

Examples attached.

```html
<!DOCTYPE html>
<html lang="en">
<head>
<meta charset="utf-8">
<title>Plinkr Leaderboard Banners</title>
<link rel="stylesheet" href="https://fonts.googleapis.com/css2?family=Figtree:wght@400;600;700;800&display=swap">
<style>
  :root {
    --stage: #8d8e90;
    --paper: #f6f7f8;
    --paper-shade: #eceef1;
    --brand-blue: #0a6aa8;
    --brand-orange: #e46400;
    --stripe-blue: #9fc2da;
    --white: #ffffff;
  }
  * { margin: 0; padding: 0; box-sizing: border-box; }
  html, body {
    width: 1200px;
    height: 966px;
    overflow: hidden;
    background: var(--stage);
    font-family: "Figtree", sans-serif;
  }
  .canvas { position: relative; width: 1200px; height: 966px; }
  .banner { position: absolute; display: block; }
  .banner--728 { left: 210px; width: 780px; height: 97px; }
  .banner--960 { left: 86px; width: 1029px; height: 97px; }
  .banner--marketing-728 { top: 155px; }
  .banner--hr-728 { top: 315px; }
  .banner--marketing-960 { top: 549px; }
  .banner--hr-960 { top: 719px; }

  .paper { fill: url(#paperGradient); }
  .band--blue { fill: var(--brand-blue); }
  .band--orange { fill: var(--brand-orange); }
  .accent-stripe { fill: url(#stripeGradient); }
  .divider { stroke: var(--white); stroke-width: 2; }

  .brand-name {
    fill: var(--brand-blue);
    font-weight: 800;
    letter-spacing: 0.5px;
  }
  .strap { fill: var(--white); }
  .strap__lead { font-weight: 400; letter-spacing: -0.3px; }
  .strap__main { font-weight: 700; letter-spacing: -0.2px; }
  .cta__pill--orange { fill: var(--brand-orange); }
  .cta__pill--blue { fill: var(--brand-blue); }
  .cta__label {
    fill: var(--white);
    font-weight: 600;
    font-size: 14px;
    letter-spacing: 0.3px;
  }
</style>
</head>
<body>
<main class="canvas">

  <svg width="0" height="0" style="position:absolute" aria-hidden="true">
    <defs>
      <linearGradient id="paperGradient" x1="0" y1="0" x2="1" y2="1">
        <stop offset="0" stop-color="#f8f9fa"/>
        <stop offset="1" stop-color="#eceef1"/>
      </linearGradient>
      <linearGradient id="stripeGradient" x1="0" y1="0" x2="0" y2="1">
        <stop offset="0" stop-color="#cfe0ec"/>
        <stop offset="1" stop-color="#7fb0d2"/>
      </linearGradient>
    </defs>
  </svg>

  <!-- Marketing Plinkr 728 -->
  <svg class="banner banner--728 banner--marketing-728" viewBox="0 0 780 97" role="img" aria-label="Marketing Plinkr banner: Your No.1 Whitepaper Resource, Click Here">
    <rect class="paper" width="780" height="97"/>
    <text class="brand-name" x="40" y="44" font-size="26">MARKETING</text>
    <text class="brand-name" x="40" y="76" font-size="26">PLINKR</text>
    <path class="band--blue" d="M233 0 H458 L612 43 Q624 47 620 62 L612 97 H205 Z"/>
    <line class="divider" x1="263" y1="21" x2="263" y2="81"/>
    <text class="strap strap__lead" x="276" y="45" font-size="29">Your No.1</text>
    <text class="strap strap__main" x="276" y="77" font-size="28">Whitepaper Resource</text>
    <rect class="cta__pill--orange" x="628" y="54" width="126" height="28" rx="14"/>
    <text class="cta__label" x="691" y="73" text-anchor="middle">CLICK HERE</text>
  </svg>

  <!-- HR Plinkr 728 -->
  <svg class="banner banner--728 banner--hr-728" viewBox="0 0 780 97" role="img" aria-label="HR Plinkr banner: Essential Whitepapers for HR Professionals, Click Here">
    <rect class="paper" width="780" height="97"/>
    <text class="brand-name" x="40" y="44" font-size="30">HR</text>
    <text class="brand-name" x="40" y="78" font-size="30">PLINKR</text>
    <path class="accent-stripe" d="M226 0 H242 L210 97 H193 Z"/>
    <path class="band--orange" d="M242 0 H703 L671 97 H210 Z"/>
    <path class="accent-stripe" d="M703 0 H723 L688 97 H671 Z"/>
    <line class="divider" x1="278" y1="20" x2="278" y2="80"/>
    <text class="strap strap__lead" x="292" y="46" font-size="29">Essential Whitepapers for</text>
    <text class="strap strap__main" x="292" y="80" font-size="29">HR Professionals</text>
    <rect class="cta__pill--blue" x="628" y="53" width="126" height="28" rx="14"/>
    <text class="cta__label" x="691" y="72" text-anchor="middle">CLICK HERE</text>
  </svg>

  <!-- Marketing Plinkr 960 -->
  <svg class="banner banner--960 banner--marketing-960" viewBox="0 0 1029 97" role="img" aria-label="Marketing Plinkr wide banner: Your No.1 Whitepaper Resource, Click Here">
    <rect class="paper" width="1029" height="97"/>
    <text class="brand-name" x="62" y="44" font-size="26">MARKETING</text>
    <text class="brand-name" x="62" y="76" font-size="26">PLINKR</text>
    <path class="band--blue" d="M298 0 H641 L800 48 Q812 52 809 66 L802 97 H271 Z"/>
    <line class="divider" x1="366" y1="17" x2="366" y2="85"/>
    <text class="strap strap__lead" x="381" y="42" font-size="33">Your No.1</text>
    <text class="strap strap__main" x="381" y="80" font-size="32">Whitepaper Resource</text>
    <rect class="cta__pill--orange" x="845" y="54" width="127" height="28" rx="14"/>
    <text class="cta__label" x="908.5" y="73" text-anchor="middle">CLICK HERE</text>
  </svg>

  <!-- HR Plinkr 960 -->
  <svg class="banner banner--960 banner--hr-960" viewBox="0 0 1029 97" role="img" aria-label="HR Plinkr wide banner: Essential Whitepapers for HR Professionals, Click Here">
    <rect class="paper" width="1029" height="97"/>
    <text class="brand-name" x="62" y="44" font-size="30">HR</text>
    <text class="brand-name" x="62" y="78" font-size="30">PLINKR</text>
    <path class="accent-stripe" d="M260 0 H279 L247 97 H229 Z"/>
    <path class="band--orange" d="M279 0 H823 L791 97 H247 Z"/>
    <path class="accent-stripe" d="M823 0 H843 L808 97 H791 Z"/>
    <line class="divider" x1="334" y1="17" x2="334" y2="84"/>
    <text class="strap strap__lead" x="350" y="45" font-size="33">Essential Whitepapers for</text>
    <text class="strap strap__main" x="350" y="83" font-size="33">HR Professionals</text>
    <rect class="cta__pill--blue" x="845" y="54" width="127" height="28" rx="14"/>
    <text class="cta__label" x="908.5" y="73" text-anchor="middle">CLICK HERE</text>
  </svg>

</main>
</body>
</html>
```